Business Card Design Project for Architecture and Interior Design company

We need a business card design and logo for an architecture and design firm located in Santiago de Chile. It´s a small company, and the name is "Vostiq" ("Vost" from my surname Vostani, and "arq" for arquitectura or architecture. But it would also be nice that the logo comunicates de Word game "Vosta" as beautiful in italian, and "arq" as architecture".
The idea is to give a delicate, elegant and sofisticated, yet fresh image. Would prefer grey black and white colors, but wouldn´t mind to use another additional color.
I allready have a web page www.vostiq.cl, but would like to improve the logo design.
Please contact if any further information is requiered.
Reason: Need a more arquitectural and desing spirit in the cards. Few of them give that idea.

```html
<!DOCTYPE html>
<html lang="en">
<head>
<meta charset="utf-8">
<title>Vostiq — Business Card</title>
<link rel="stylesheet" href="https://fonts.googleapis.com/css2?family=Fira+Sans+Condensed:wght@400;600&display=swap">
<style>
  :root {
    --page: #ffffff;
    --ink: #1e1b14;
    --wall-light: #f1f0ea;
    --wall-mid: #d9d8cf;
    --wall-shade: #b9bab3;
    --floor-light: #f2efdc;
    --floor-mid: #cfcab2;
    --panel: rgba(238, 234, 214, 0.72);
    --panel-edge: #c9b57e;
    --card-edge: #3a3628;
  }
  * { box-sizing: border-box; margin: 0; padding: 0; }
  html, body {
    width: 1200px; height: 800px; overflow: hidden;
    background: var(--page);
  }
  .canvas { position: relative; width: 1200px; height: 800px; }

  .card {
    position: absolute;
    width: 560px; height: 315px;
    border: 1px solid var(--card-edge);
    overflow: hidden;
  }
  .card--front { left: 50px; top: 60px; }
  .card--back  { left: 590px; top: 420px; }

  .room-render {
    position: absolute; inset: 0;
  }
  .card--front .room-render {
    background:
      linear-gradient(180deg, var(--wall-light) 0%, var(--wall-mid) 52%, var(--floor-light) 58%, var(--floor-mid) 100%);
  }
  .card--back .room-render {
    background:
      linear-gradient(180deg, var(--floor-light) 0%, #e6e3cf 45%, var(--wall-shade) 52%, #e4e0c9 62%, var(--floor-light) 100%);
  }

  .wordmark {
    position: absolute;
    font-family: "Fira Sans Condensed", sans-serif;
    font-weight: 600;
    color: var(--ink);
    letter-spacing: -0.5px;
    line-height: 1;
  }
  .card--front .wordmark { left: 168px; top: 132px; font-size: 66px; }
  .card--back .wordmark  { left: 16px; top: 14px; font-size: 76px; }

  .panel {
    position: absolute;
    background: var(--panel);
    border: 1px solid var(--panel-edge);
  }
  .panel--top-left   { left: 0; top: 0; width: 100px; height: 150px; }
  .panel--top-right  { left: 150px; top: 0; width: 410px; height: 150px; }
  .panel--bottom-left  { left: 0; top: 190px; width: 100px; height: 125px; }
  .panel--bottom-right { left: 150px; top: 190px; width: 410px; height: 125px; }
  .panel--corner { left: 370px; top: 0; width: 190px; height: 150px; background: rgba(230, 226, 206, 0.5); }

  .contact {
    position: absolute;
    right: 60px; bottom: 16px;
    display: grid;
    grid-template-columns: auto auto;
    column-gap: 10px;
    font-family: "Fira Sans Condensed", sans-serif;
    font-size: 11.5px;
    line-height: 15px;
    color: var(--ink);
  }
  .contact dt { font-weight: 600; text-align: right; }
  .contact dd { font-weight: 400; }
</style>
</head>
<body>
<main class="canvas">

  <section class="card card--front" aria-label="Business card front">
    <div class="room-render" role="img" aria-label="Rendered empty white room with light wooden plank floor and sunlight through a window"></div>
    <div class="wordmark">Vostiq</div>
  </section>

  <section class="card card--back" aria-label="Business card back">
    <div class="room-render" role="img" aria-label="Rendered interior with white walls and wooden floor seen behind translucent panels"></div>
    <div class="panel panel--top-left"></div>
    <div class="panel panel--top-right"></div>
    <div class="panel panel--corner"></div>
    <div class="panel panel--bottom-left"></div>
    <div class="panel panel--bottom-right"></div>
    <div class="wordmark">Vostiq</div>
    <dl class="contact">
      <dt>Name:</dt><dd>First Middle Last</dd>
      <dt>Title:</dt><dd>Chief Executive Officer</dd>
      <dt>Cell Phone :</dt><dd>148 620 371</dd>
      <dt>Toll-Free :</dt><dd>312 406 985</dd>
      <dt>E-mail address:</dt><dd>example@vostiq.cl</dd>
      <dt>website URL:</dt><dd>www.vostiq.cl</dd>
    </dl>
  </section>

</main>
</body>
</html>
```